Forensic Psychology and Polygraph Needs Clever Catchy Logo

There's a massive trade show coming up and we are looking to debut a new, clever logo for our business cards. We are a private practice that offers psychological evaluations, therapeutic counseling, and polygraphing. Our website is kelvora.net (to get a better idea of the color scheme) and instead of the nature/cuddly image that other psychology organizations like to go for, we are interested in cultivating a business, strength, and professional image.
Attached are some popular logos and designs to get those creative juices flowing! I would like to avoid the brain/psi logo as this has been to death so bonus points definitely for originality.
Target Market(s)
governmental agencies, third party mental health providers, individual private pay clients
Industry/Entity Type
Mental Health
Contact Information for Business Card
One one side will be the logo and company name while on the back will be contact information and provider details (name, position, etc)
Look and feel
Each slider illustrates characteristics of the customer's brand and the style your logo design should communicate.

```html
<!DOCTYPE html>
<html lang="en">
<head>
<meta charset="utf-8">
<title>Marlow &amp; Associates — Business Card</title>
<link rel="stylesheet" href="https://fonts.googleapis.com/css2?family=Cinzel:wght@400;600&family=Questrial&family=Open+Sans:wght@600&display=swap">
<style>
  :root {
    --backdrop: #000000;
    --card-white: #ffffff;
    --teal: #1fb3b3;
    --teal-bright: #1ab8b6;
    --slate: #545865;
    --ink: #2f2c33;
    --ink-soft: #4a4750;
    --rule: #bfe9ea;
  }
  * { box-sizing: border-box; margin: 0; padding: 0; }
  html, body { width: 1200px; height: 900px; overflow: hidden; background: var(--backdrop); }
  .stage { position: relative; width: 1200px; height: 900px; }

  .card {
    position: absolute; top: 192px; height: 491px; border-radius: 16px; overflow: hidden;
  }
  .card--front { left: 295px; width: 301px; background: var(--card-white); }
  .card--back {
    left: 621px; width: 305px;
    background: radial-gradient(ellipse 62% 58% at 50% 46%, var(--teal-bright) 0%, #1b8f93 45%, var(--slate) 100%);
  }

  .line { position: absolute; left: 0; width: 100%; text-align: center; white-space: nowrap; }

  .brand-dot { position: absolute; border-radius: 50%; }
  .card--front .brand-dot { left: 100px; top: 72px; width: 82px; height: 82px; background: var(--teal); }
  .card--back .brand-dot { left: 106px; top: 180px; width: 78px; height: 78px; background: var(--card-white); }

  .brand-name { font-family: "Cinzel", serif; font-weight: 400; font-size: 19px; letter-spacing: 0.2px; }
  .brand-tagline { font-family: "Questrial", sans-serif; font-size: 11px; letter-spacing: 0.6px; }
  .card--front .brand-name { top: 164px; color: var(--ink); }
  .card--front .brand-tagline { top: 188px; color: var(--ink-soft); }
  .card--back .brand-name { top: 270px; color: var(--card-white); }
  .card--back .brand-tagline { top: 293px; color: var(--card-white); }

  .person-name { top: 276px; font-family: "Cinzel", serif; font-weight: 600; font-size: 21px; color: var(--teal); letter-spacing: 0.5px; }
  .person-role { top: 302px; font-family: "Questrial", sans-serif; font-size: 13px; color: var(--ink-soft); letter-spacing: 0.4px; }

  .contact { font-family: "Questrial", sans-serif; font-size: 14px; color: var(--ink-soft); }
  .contact b { color: var(--teal); font-weight: 700; }
  .contact--phone { top: 336px; }
  .contact--email { top: 356px; }
  .contact-rule { position: absolute; left: 70px; width: 161px; top: 380px; height: 1px; background: var(--rule); }
  .address { font-family: "Questrial", sans-serif; font-size: 14px; color: var(--ink-soft); line-height: 18px; }
  .address--1 { top: 388px; }
  .address--2 { top: 406px; }
  .address--3 { top: 424px; }

  .services { font-family: "Open Sans", sans-serif; font-weight: 600; font-size: 14px; color: var(--card-white); }
  .services--1 { top: 391px; }
  .services--2 { top: 411px; }
</style>
</head>
<body>
<main class="stage">
  <section class="card card--front" aria-label="Card front with contact details">
    <span class="brand-dot" aria-hidden="true"></span>
    <p class="line brand-name">MARLOW &amp; ASSOCIATES</p>
    <p class="line brand-tagline">PSYCHOLOGICAL SERVICES</p>
    <p class="line person-name">DORIAN HALE</p>
    <p class="line person-role">DIRECTOR</p>
    <p class="line contact contact--phone"><b>P:</b> 602.555.0183</p>
    <p class="line contact contact--email"><b>E:</b> contact@kelvora.net</p>
    <span class="contact-rule" aria-hidden="true"></span>
    <p class="line address address--1">2280 E. Cactus Ridge Rd.</p>
    <p class="line address address--2">Suites 204 and 208 Phoenix,</p>
    <p class="line address address--3">Arizona 85016</p>
  </section>

  <section class="card card--back" aria-label="Card back with company name and services">
    <span class="brand-dot" aria-hidden="true"></span>
    <p class="line brand-name">MARLOW &amp; ASSOCIATES</p>
    <p class="line brand-tagline">PSYCHOLOGICAL SERVICES</p>
    <p class="line services services--1">THERAPY | EVALUATIONS</p>
    <p class="line services services--2">CONSULTATION</p>
  </section>
</main>
</body>
</html>
```